Webdesign für Konfigurator für individuelle Nahrungsergänzungsmittel
Zielgruppe
Die Sternperle (sternperle.de) ist Deutschlands erster Konfigurator für individuelle Nahrungsergänzungsmittel.
Wir stellen jedes Produkt von Hand her und fertigen ausschließlich in unserer Manufaktur in Halvenbrück. Jedes hergestellte Produkt ist individualisiert und trägt den Namen des Käufers.
Unsere Kunden/Kundinnen (ab jetzt ohne Gendern weiter, das wird sonst so sperrig) können sich aus über 180 Rohstoffen bedienen, diese frei kombinieren und von uns in eine Kapsel pressen lassen. Nicht nur die Inhaltsstoffe, auch die Farbe der Kapseln und auch unsere nachhaltige Verpackung (aus Papier und Kork) kann individuell gestaltet werden. Unsere Kunden sind Endkunden, Therapeuten und Händler.
*Wer sind unsere Kunden:
1.) Endkunden mit bekannten Problemen oder dem Wunsch, sich und seinem Körper etwas Gutes zu tun. ('Ich möchte meine Haut und mein Immunsystem unterstützen.')
2.) Endkunden, welche bereits ein oder mehrere Nahrungsergänzungen einnehmen und diese Einnahme vereinfachen wollen ('Nun alles in einer Kapsel')
3.) Endkunden, welche direkte Empfehlungen erhalten haben ('Nimm dies und das.')
4.) Ärzte, Heilpraktiker, Mykotherapeuten, Physiotherapeuten, Ernährungsberater, andere Heilberufe: wir bieten ein spannendes Partnerprogramm, welches dem Therapeuten erlaubt, Nahrungsergänzungen direkt für die Patienten zu konfigurieren. Der Fachmann wählt also die passenden Inhaltsstoffe aus unserem Portfolio aus. Die Dose trägt das Logo, den Namen und die Farbe der jeweiligen Praxis (wird mit dem Kundenkonto verknüpft). Der Patient bekommt eine Vorkasse-Rechnung vom Therapeuten mit und zahlt direkt an die Sternperle, welche das Paket nach Geldeingang direkt an den Patienten versendet. Der Therapeut profitiert durch sein Corporate Design wie auch durch eine Provision.
5.) Händler. Als Manufaktur bieten wir Kleinunternehmern die Möglichkeit, eigene Produkte für den Weiterverkauf herzustellen. Anders als große Loh..
Aufgabenstellung
Logo und CI kann dem bisherigen Design entnommen werden.
Die 'Löffel-Illustration' muss in Grundzügen übernommen werden, kann aber durchaus verändert werden.
Unsere Plattform ist Shopware 6.
Die verwendete Schriftarten sind Bitter und Calibri - dies ist aber nicht verpflichtend.

```html
<!DOCTYPE html>
<html lang="de">
<head>
<meta charset="utf-8">
<title>Sternperle – Partnerprogramm</title>
<link href="https://fonts.googleapis.com/css2?family=Bitter:ital,wght@0,400;0,500;0,600;1,400&family=Carlito:wght@400;700&display=swap" rel="stylesheet">
<style>
  :root{
    --teal:#108a80;
    --teal-soft:#4aa39c;
    --red:#d43b45;
    --ink:#1f1f1f;
    --grey:#7a7a7a;
    --band:#f1f4f3;
    --warm-top:#ece9e5;
    --warm:#f4f3f0;
    --cool-top:#e6ecee;
    --cool:#f0f4f4;
    --line:#a9d4cf;
  }
  *{margin:0;padding:0;box-sizing:border-box}
  html,body{width:870px;height:1200px;overflow:hidden;background:#fff}
  .page{position:absolute;left:0;top:0;width:1640px;height:2262px;transform:scale(.5305);transform-origin:0 0;font-family:Carlito,Calibri,sans-serif;color:var(--ink)}
  .abs{position:absolute}
  .serif{font-family:Bitter,Georgia,serif}
  .btn{position:absolute;background:var(--red);color:#fff;font-family:Carlito,sans-serif;font-size:19px;letter-spacing:1.5px;display:flex;align-items:center;justify-content:center;box-shadow:2px 3px 6px rgba(0,0,0,.2)}
  .social-band{left:135px;top:0;width:1372px;height:96px;background:var(--band)}
  .thumb{top:0;width:250px;height:38px}
  .main-title{left:0;width:1640px;top:218px;text-align:center;font-family:Bitter,serif;font-weight:600;font-size:56px;color:var(--teal)}
  .card-top{top:331px;width:676px;height:382px}
  .card-body{top:717px;width:676px;height:828px}
  .audience{font-family:Bitter,serif;font-weight:600;font-size:24px;position:absolute;left:27px;top:34px}
  .audience-list{position:absolute;left:25px;top:81px;list-style:none;font-size:19px;line-height:21.2px;color:var(--grey)}
  .portrait{position:absolute;left:319px;top:33px;width:314px;height:314px;border-radius:50%}
  .pitch{position:absolute;left:58px;top:29px;font-family:Bitter,serif;font-weight:500;font-size:25px;line-height:35px;color:var(--teal)}
  .pitch-text{position:absolute;left:58px;top:118px;width:580px;font-size:18.6px;line-height:24px}
  .icon{position:absolute;top:313px}
  .benefit{position:absolute;top:395px;text-align:center}
  .benefit h3{font-family:Bitter,serif;font-weight:500;font-size:25px;color:var(--teal);margin-bottom:10px}
  .benefit p{font-size:14.6px;line-height:19px}
  .rule{position:absolute;height:1px;background:var(--line)}
  .extras-label{position:absolute;top:536px;left:255px;width:165px;text-align:center;font-family:Bitter,serif;font-size:16px;color:var(--red)}
  .extra{position:absolute;top:588px;width:220px;text-align:center}
  .extra span{display:block;margin-top:14px;font-family:Bitter,serif;font-weight:600;font-size:16px;color:var(--teal)}
  .news-title{left:278px;top:1614px;font-family:Bitter,serif;font-weight:500;font-size:25px;line-height:35px;color:var(--teal)}
  .news-visual{left:362px;top:1700px;width:278px;height:80px;border-radius:40px;background:linear-gradient(90deg,#cfe5ea,#e9f3f5 60%,#d5e8ec)}
  .brand{font-family:Bitter,serif;font-weight:600;font-size:26px;color:var(--teal)}
  .email{left:830px;top:1618px;width:520px;height:65px;border:1.5px solid var(--line);background:#fff;padding-left:32px;display:flex;align-items:center;font-family:Bitter,serif;font-style:italic;font-size:17px;color:#555}
  .consent{left:832px;top:1700px;font-size:15px;line-height:24px}
  .consent .box{position:absolute;left:0;top:1px;width:19px;height:19px;border:1.5px solid var(--red);border-radius:3px;background:#fff}
  .consent p{margin-left:27px}
  .consent a{color:var(--teal)}
  .footer-col h4{font-family:Bitter,serif;font-weight:600;font-size:17px;color:var(--teal);margin-bottom:26px}
  .footer-col li{list-style:none;font-size:15px;line-height:24px}
  .notes{left:1040px;top:1983px;width:430px;font-family:Bitter,serif;font-style:italic;font-size:13px;line-height:20px;color:#666}
  .legal{top:2180px;font-size:11.5px;letter-spacing:.8px;color:var(--teal)}
  .chip{position:absolute;top:2175px;height:22px;border-radius:3px;font-size:11px;font-weight:700;display:flex;align-items:center;justify-content:center;color:#fff}
</style>
</head>
<body>
<div class="page">

  <!-- social band -->
  <div class="abs social-band"></div>
  <div class="btn" style="left:278px;top:0;width:171px;height:38px">FOLGE UNS</div>
  <div class="abs thumb" style="left:586px;background:linear-gradient(90deg,#8f918c,#a9aaa5)" role="img" aria-label="Social-Media-Foto mit Kapseldosen"></div>
  <div class="abs thumb" style="left:861px;background:#7d907c" role="img" aria-label="Social-Media-Beitrag auf grünem Hintergrund"></div>
  <div class="abs thumb" style="left:1135px;background:linear-gradient(90deg,#b7a18b 50%,#d7d6de 50%,#d7d6de 97%,#b79d80 97%)" role="img" aria-label="Social-Media-Foto mit Produktverpackung"></div>

  <h1 class="abs main-title">Unser Partnerprogramm mit Mehrwert(en)</h1>

  <!-- Fachleute -->
  <section class="abs card-top" style="left:135px;background:var(--warm-top)">
    <h2 class="audience">Für Fachleute</h2>
    <ul class="audience-list">
      <li>– Ärzte</li><li>– Heilpraktiker</li><li>– Mykotherapeuten</li><li>– Physiotherapeuten</li><li>– Ernährungsberater</li><li>– allg. Heilberufe</li>
    </ul>
    <div class="portrait" style="background:radial-gradient(circle at 50% 45%,#7d6e5a,#5f6e54 55%,#c9a33a 85%)" role="img" aria-label="Porträtfoto einer lächelnden Therapeutin"></div>
  </section>
  <section class="abs card-body" style="left:135px;background:var(--warm)">
    <h2 class="pitch">Profitiere durch Dein Corporate Design<br>und erhalte eine Provision.</h2>
    <p class="pitch-text">Wir bieten ein spannendes Partnerprogramm, welches Dir erlaubt, Nahrungsergänzungen direkt für Deine Patienten zu konfigurieren. Du wählent die passenden Inhaltsstoffe aus unserem Portfolio aus. Die Dose trägt das Logo, den Namen und die Farbe Deiner Praxis (wird mit dem Kundenkonto verknüpft). Dein/e Patient*in bekommt eine Vorkasse-Rechnung mit und zahlt direkt an die Sternperle, welche das Paket nach Geldeingang direkt an den Patienten versendet.</p>

    <svg class="icon" style="left:124px" width="56" height="62" viewBox="0 0 56 62"><circle cx="28" cy="15" r="14" fill="var(--red)"/><path d="M2 62V46c0-10 8-16 18-16h16c10 0 18 6 18 16v16z" fill="var(--teal-soft)"/><circle cx="17" cy="50" r="5" fill="none" stroke="#fff" stroke-width="3"/><path d="M34 56v-8a5 5 0 0 1 10 0v8" fill="none" stroke="#fff" stroke-width="3"/></svg>
    <svg class="icon" style="left:423px" width="86" height="62" viewBox="0 0 86 62"><circle cx="14" cy="18" r="9" fill="var(--red)"/><circle cx="72" cy="18" r="9" fill="var(--red)"/><circle cx="43" cy="15" r="14" fill="var(--red)"/><path d="M0 46c0-10 6-16 14-16s14 6 14 16z M58 46c0-10 6-16 14-16s14 6 14 16z" fill="var(--teal-soft)"/><path d="M17 62V48c0-10 8-16 18-16h16c10 0 18 6 18 16v14z" fill="var(--teal-soft)"/></svg>

    <div class="benefit" style="left:30px;width:260px"><h3>Vorteile für Dich...</h3><p>Dein Vorteil ist eine reiche Auswahl an<br>Inhaltsstoffen und unser attraktives<br>Vergütungssystem!</p></div>
    <div class="benefit" style="left:305px;width:320px"><h3>... und für Deine Patienten</h3><p>Deine Patienten profitieren von der<br>Herstellung in Deutschland, schneller Lieferung<br>und deinem individuellen Rabattcode</p></div>

    <div class="rule" style="left:55px;top:547px;width:200px"></div>
    <div class="extras-label">+ diese Extras</div>
    <div class="rule" style="left:420px;top:547px;width:203px"></div>

    <div class="extra" style="left:71px"><svg width="44" height="42" viewBox="0 0 44 42"><path d="M8 4h28v20H8z" fill="var(--red)"/><path d="M2 16l20 14 20-14v26H2z" fill="var(--teal-soft)"/><text x="22" y="20" text-anchor="middle" font-size="15" font-weight="700" fill="#fff" font-family="Carlito">$</text></svg><span>Kontinuierliche Vergütung</span></div>
    <div class="extra" style="left:279px"><svg width="44" height="42" viewBox="0 0 44 42"><path d="M22 22V12" stroke="var(--red)" stroke-width="3"/><path d="M22 12c-6 0-10-4-10-9 6 0 10 4 10 9zM22 12c5 0 9-4 9-9-5 0-9 4-9 9z" fill="var(--red)"/><path d="M4 30l8-4h12c3 0 3 4 0 4h-8 10l12-6c3-1 5 2 2 4L26 38H4z" fill="var(--teal-soft)"/></svg><span>Rabatt für Patienten</span></div>
    <div class="extra" style="left:436px"><svg width="44" height="42" viewBox="0 0 44 42"><path d="M2 22h40v18H2z" fill="var(--teal-soft)"/><path d="M6 28h32M6 34h32" stroke="#fff" stroke-width="2"/><path d="M14 6l4-4 18 18-4 4z" fill="var(--red)"/></svg><span>Rezeptblock</span></div>

    <div class="rule" style="left:55px;top:689px;width:568px"></div>
    <div class="btn" style="left:253px;top:740px;width:171px;height:38px">MEHR ERFAHREN</div>
  </section>

  <!-- Händler -->
  <section class="abs card-top" style="left:830px;background:var(--cool-top)">
    <h2 class="audience">Für Händler</h2>
    <div class="portrait" style="background:radial-gradient(circle at 50% 50%,#b98a6c,#d9d2c6 55%,#ecebe6 85%)" role="img" aria-label="Porträtfoto eines telefonierenden Händlers"></div>
  </section>
  <section class="abs card-body" style="left:830px;background:var(--cool)">
    <h2 class="pitch">Profitiere durch flexible Chargen<br>und White Labels-Produktion.</h2>
    <p class="pitch-text" style="width:590px">Als Manufaktur bieten wir Dir als Kleinunternehmer die Möglichkeit, eigene Produkte für den Weiterverkauf herzustellen. Anders als große Lohnhersteller können wir auch Klein- und Kleinstchargen (ab 300 Kapseln) herstellen, welche wir im Bulk, in unseren Standarddosen mit Wunsch-etikett oder in beigestellten Verpackungen abfüllen können.</p>

    <svg class="icon" style="left:122px" width="56" height="62" viewBox="0 0 56 62"><circle cx="28" cy="15" r="14" fill="var(--red)"/><path d="M2 62V46c0-10 8-16 18-16h16c10 0 18 6 18 16v16z" fill="var(--teal-soft)"/><path d="M24 32l4 8 4-8z" fill="#fff"/></svg>
    <svg class="icon" style="left:422px" width="86" height="62" viewBox="0 0 86 62"><circle cx="14" cy="18" r="9" fill="var(--red)"/><circle cx="72" cy="18" r="9" fill="var(--red)"/><circle cx="43" cy="15" r="14" fill="var(--red)"/><path d="M0 46c0-10 6-16 14-16s14 6 14 16z M58 46c0-10 6-16 14-16s14 6 14 16z" fill="var(--teal-soft)"/><path d="M17 62V48c0-10 8-16 18-16h16c10 0 18 6 18 16v14z" fill="var(--teal-soft)"/></svg>

    <div class="benefit" style="left:30px;width:260px"><h3>Vorteile für Dich...</h3><p>Dein Vorteil ist eine reiche Auswahl an<br>Inhaltsstoffen und unser attraktives<br>Vergütungssystem!</p></div>
    <div class="benefit" style="left:305px;width:320px"><h3>... und für Deine Kunden</h3><p>Deine Patienten profitieren von der<br>Herstellung in Deutschland, schneller Lieferung<br>und deinem individuellen Rabattcode</p></div>

    <div class="rule" style="left:53px;top:547px;width:200px"></div>
    <div class="extras-label" style="left:253px">+ diese Extras</div>
    <div class="rule" style="left:418px;top:547px;width:203px"></div>

    <div class="extra" style="left:69px"><svg width="44" height="42" viewBox="0 0 44 42"><path d="M8 4h28v20H8z" fill="var(--red)"/><path d="M2 16l20 14 20-14v26H2z" fill="var(--teal-soft)"/><text x="22" y="20" text-anchor="middle" font-size="15" font-weight="700" fill="#fff" font-family="Carlito">$</text></svg><span>Kontinuierliche Vergütung</span></div>
    <div class="extra" style="left:277px"><svg width="44" height="42" viewBox="0 0 44 42"><path d="M22 22V12" stroke="var(--red)" stroke-width="3"/><path d="M22 12c-6 0-10-4-10-9 6 0 10 4 10 9zM22 12c5 0 9-4 9-9-5 0-9 4-9 9z" fill="var(--red)"/><path d="M4 30l8-4h12c3 0 3 4 0 4h-8 10l12-6c3-1 5 2 2 4L26 38H4z" fill="var(--teal-soft)"/></svg><span>Rabatt für Kunden</span></div>
    <div class="extra" style="left:434px"><svg width="44" height="42" viewBox="0 0 44 42"><path d="M2 22h40v18H2z" fill="var(--teal-soft)"/><path d="M6 28h32M6 34h32" stroke="#fff" stroke-width="2"/><path d="M14 6l4-4 18 18-4 4z" fill="var(--red)"/></svg><span>Rezeptblock</span></div>

    <div class="rule" style="left:53px;top:689px;width:568px"></div>
    <div class="btn" style="left:251px;top:740px;width:171px;height:38px">MEHR ERFAHREN</div>
  </section>

  <!-- Newsletter -->
  <h2 class="abs news-title">Abboniere unseren Sternperle Newsletter<br>und erfähre alle Neuigkeiten als Erstes!</h2>
  <div class="abs news-visual" role="img" aria-label="Hellblaue Kapseln verstreut auf weißem Grund"></div>
  <div class="abs brand" style="left:410px;top:1782px">Sternperle</div>

  <div class="abs email">max@mustermann.de</div>
  <div class="abs consent"><span class="box"></span><p>Ich habe die <a href="#">Datenschutzbestimmungen</a> zur Kenntnis genommen<br>und die <a href="#">AGB</a> gelesen und bin mit ihnen einverstanden.</p></div>
  <div class="btn" style="left:1178px;top:1768px;width:171px;height:38px">JETZT ANMELDEN</div>

  <!-- Footer -->
  <div class="rule" style="left:190px;top:1893px;width:1272px"></div>
  <nav class="abs footer-col" style="left:193px;top:1933px"><h4>Sternperle</h4><ul><li>Sternperle-Konfigurator</li><li>Was ist die Sternperle</li><li>Sternperle für Dich</li><li>Sternperle für Fachleute</li><li>Sternperle für Händler</li><li>FAQ</li></ul></nav>
  <nav class="abs footer-col" style="left:416px;top:1933px"><h4>Shop Service</h4><ul><li>Shop</li><li>Pur-Produkte</li><li>Synergie-Produkte</li><li>Premium-Produkte</li><li>Omega-Fettsäure-Konzentrate</li><li>Geschenkgutscheine</li></ul></nav>
  <nav class="abs footer-col" style="left:649px;top:1933px"><h4>Manufaktur</h4><ul><li>Über uns</li><li>Das Team</li><li>Die Philosophie</li><li>Karriere</li><li>Presse</li><li>Kontakt</li></ul></nav>
  <nav class="abs footer-col" style="left:808px;top:1933px"><h4>Informationen</h4><ul><li>Versand &amp; Zahlung</li><li>Bewertungen</li><li>Datenschutz-Einstellungen</li></ul></nav>

  <div class="abs" style="left:1233px;top:1918px;width:30px;height:30px;border-radius:50%;background:var(--ink)"></div>
  <div class="abs serif" style="left:1272px;top:1912px;font-style:italic;font-size:28px;color:var(--red)">#sternperle</div>

  <div class="abs notes"><p>* Alle Preise inkl. gesetzl. Mehrwertsteuer zzgl. Versandkosten und ggf. Nachnahmegebühren, wenn nicht anders angegeben.</p><p style="margin-top:19px">** Prozentwert der EU-weit geltenden Referenzmenge (Nutrition Reference Values) für Vitamine und Mineralstoffe in Lebensmitteln pro Tag</p></div>

  <div class="abs legal" style="left:193px">AGB</div>
  <div class="abs legal" style="left:231px">WIDERRUF</div>
  <div class="abs legal" style="left:301px">DATENSCHUTZ</div>
  <div class="abs legal" style="left:398px">IMPRESSUM</div>
  <div class="abs legal" style="left:1033px">ZAHLUNGSMITTEL</div>

  <div class="chip" style="left:1166px;width:98px;color:var(--ink);font-size:14px">Kaufpilot</div>
  <div class="chip" style="left:1268px;width:32px;background:#eef0f4;color:var(--ink);font-size:8px">Zahl</div>
  <div class="chip" style="left:1310px;width:30px;background:#eeb8c9;color:var(--ink);font-size:8px">Rate</div>
  <div class="chip" style="left:1351px;width:32px;background:#1d3f8f;font-size:8px">Konto</div>
  <div class="chip" style="left:1392px;width:32px;background:#eef0f4;color:var(--ink);font-size:7px">Lastsch</div>
  <div class="chip" style="left:1433px;width:32px;background:#d93f8a"></div>

  <div class="abs serif" style="left:0;width:1640px;top:2225px;text-align:center;font-style:italic;font-size:13px;color:#555">© Sternperle GmbH | 2022</div>
</div>
</body>
</html>
```